Records Management Company Revamp

We are looking to revamp our web presence, and need a catchy design that helps us to get noticed! We would like the website to be in wordpress. the main requirements are a home page, a landing page template for SEO / PPC, and then a few other pages that can be reused throughout the website.

We are happy to supply content / video etc.

Number of Pages Required

3 page

Font styles to use
Other font styles liked:
• Find fonts listed in attached branding document

Requirements
Must have
• Home page as well as sub pages according to their colours. Need to use colours and fonts set out in branding guide. Attached are examples of home page and sub pages.
Nice to have
• We have uploaded some very basic ideas we have of how we wish the website to look, but looking to have it more professional and fit together. Please see uploaded items.

```html
<!DOCTYPE html>
<html lang="en">
<head>
<meta charset="utf-8">
<title>Keepsafe Archives – Archive Document Storage &amp; Records Management</title>
<link href="https://fonts.googleapis.com/css2?family=Oswald:wght@400;500;600&family=Open+Sans:wght@400;600;700&display=swap" rel="stylesheet">
<style>
:root{
  --orange:#f39a1e;
  --blue:#2f80cf;
  --blue-dark:#2469b0;
  --red:#d8342c;
  --green:#7db631;
  --ink:#2d2d2d;
  --nav:#3b3b3b;
  --navy:#17263a;
  --footer:#1e1e1e;
  --grey-bg:#f3f3f3;
  --line:#e2e2e2;
  --muted:#777;
}
*{box-sizing:border-box;margin:0;padding:0}
html,body{width:1200px;height:4452px;overflow:hidden}
body{font-family:'Open Sans',Arial,sans-serif;color:var(--ink);background:#fff;position:relative;font-size:13px;line-height:1.5}
.abs{position:absolute}
.head-font{font-family:'Oswald','Arial Narrow',sans-serif;text-transform:uppercase}
.btn{display:inline-block;background:var(--orange);color:#fff;font-family:'Oswald','Arial Narrow',sans-serif;font-size:13px;letter-spacing:.5px;padding:8px 18px;text-transform:uppercase}

/* header */
.site-header{top:0;left:0;width:1200px;height:120px;background:#fff}
.brand{display:flex;align-items:center;gap:10px;font-family:'Oswald','Arial Narrow',sans-serif;font-weight:600;font-size:30px;color:var(--ink);letter-spacing:.5px}
.brand-square{width:26px;height:26px;background:var(--ink)}
.site-header .brand{position:absolute;left:140px;top:36px}
.quote-btn{left:530px;top:38px;font-size:16px;padding:10px 22px}
.call{left:790px;top:34px;display:flex;align-items:center;gap:12px}
.call-icon{width:44px;height:44px;border-radius:50%;background:var(--ink);display:flex;align-items:center;justify-content:center}
.call small{display:block;font-size:11px;color:var(--muted);font-weight:700;line-height:1}
.call strong{font-family:'Oswald','Arial Narrow',sans-serif;font-size:24px;font-weight:500;line-height:1.1}
.cart{left:1000px;top:38px}
.main-nav{top:120px;left:0;width:1200px;height:40px;background:var(--nav);display:flex;padding-left:140px}
.main-nav a{color:#fff;font-family:'Oswald','Arial Narrow',sans-serif;font-size:14px;text-decoration:none;padding:0 20px;line-height:40px;letter-spacing:.5px}
.main-nav a.active{background:var(--orange)}

/* hero */
.hero{top:160px;left:0;width:1200px;height:580px;background:linear-gradient(100deg,#c9c3bb 0%,#8e8578 35%,#5b5550 70%,#3e3a38 100%)}
.hero-title{left:680px;top:90px;color:#fff;font-size:27px;line-height:1.2;font-weight:500}
.hero-sub{left:680px;top:160px;width:440px;color:#fff;font-size:15px;line-height:1.4}
.enquiry{left:672px;top:200px;width:456px;height:320px;background:rgba(255,255,255,.85);padding:20px 24px}
.enquiry h3{font-size:15px;font-weight:700;line-height:1.3;margin-bottom:12px}
.field{height:34px;background:#fff;border:1px solid #ccc;margin-bottom:10px;font-size:10px;color:#888;padding:0 12px;line-height:32px;font-weight:600;position:relative}
.field.select::after{content:"";position:absolute;right:14px;top:13px;border:5px solid transparent;border-top-color:#666}
.send{display:block;width:230px;margin:4px auto 0;background:var(--blue);color:#fff;font-family:'Oswald','Arial Narrow',sans-serif;font-size:18px;text-align:center;padding:8px 0}

/* services */
.services{top:752px;left:20px;width:1160px;display:flex;gap:28px}
.service{width:269px;height:348px;display:flex;flex-direction:column}
.service .photo{height:180px}
.service .body{flex:1;padding:14px 18px;color:#fff}
.service h4{font-size:17px;font-weight:500;margin-bottom:4px}
.service p{font-size:11px;line-height:1.5}
.s-red .body{background:var(--red)}.s-red .photo{background:linear-gradient(160deg,#b86a3c,#6e4226)}
.s-green .body{background:var(--green)}.s-green .photo{background:linear-gradient(160deg,#e2e2e2,#9ea3a8)}
.s-orange .body{background:var(--orange)}.s-orange .photo{background:linear-gradient(160deg,#d7d0c8,#7c7470)}
.s-blue .body{background:var(--blue)}.s-blue .photo{background:linear-gradient(160deg,#b7c8e4,#a0835a)}

/* how it works */
.band{top:1130px;left:0;width:1200px;height:14px;background:#d9d9d9}
.how{top:1144px;left:0;width:1200px;height:716px;background:var(--grey-bg)}
.section-title{font-family:'Oswald','Arial Narrow',sans-serif;text-transform:uppercase;font-size:30px;font-weight:500;color:var(--ink)}
.section-title::after{content:"";display:block;width:50px;height:3px;background:var(--ink);margin-top:6px}
.how .section-title{position:absolute;left:140px;top:64px}
.center-title{text-align:center}
.center-title::after{margin:6px auto 0}
.steps{position:absolute;left:150px;top:160px;width:420px}
.step{display:flex;gap:18px;height:92px;border-bottom:1px solid var(--line);padding-top:12px}
.step svg{flex:none}
.step h5{font-size:12px;font-weight:700;text-transform:uppercase;color:var(--ink)}
.step p{font-size:11px;color:var(--muted);line-height:1.5}
.laptop{position:absolute;left:680px;top:190px;width:500px;height:470px;background:linear-gradient(180deg,#f3f3f3,#cfd3d8 60%,#9aa1a8)}

/* team / software */
.team{top:1860px;left:0;width:730px;height:520px;background:linear-gradient(180deg,#d0d6de 0%,#6c7480 55%,#2c3138 100%)}
.team h2{position:absolute;left:140px;top:360px;color:#fff;font-size:38px;font-weight:500}
.team .btn{position:absolute;left:140px;top:424px}
.software{top:1860px;left:730px;width:470px;height:520px;background:var(--blue);color:#fff;padding:110px 60px 0 70px}
.software h2{font-size:34px;font-weight:500;margin-bottom:12px}
.software p{font-size:12px;line-height:1.6;margin-bottom:34px}

/* offers */
.offers-title{top:2380px;left:0;width:1200px}
.offers{top:2460px;left:140px;width:920px;display:flex;gap:24px}
.offer{width:448px;height:300px;position:relative;padding:70px 30px}
.offer.o-blue{background:linear-gradient(135deg,#4a95de,#2a6fb7)}
.offer.o-dark{background:linear-gradient(135deg,#4f5a66,#222a32)}
.offer h3{color:#fff;font-size:22px;font-weight:500;width:200px;line-height:1.25;margin-bottom:22px}
.offer-badge{position:absolute;right:30px;top:50px;width:190px;height:190px;border-radius:50%;background:#fff;text-align:center;font-family:'Oswald','Arial Narrow',sans-serif;color:var(--orange);padding-top:26px}
.offer-badge span{display:block;font-size:20px;line-height:1;color:var(--ink)}
.offer-badge b{display:block;font-size:70px;font-weight:500;line-height:1.05}
.offer-badge i{font-style:normal;font-size:30px;line-height:1}

/* benefits */
.benefits-title{top:2820px;left:0;width:1200px}
.benefits{top:2950px;left:310px;width:580px;display:grid;grid-template-columns:repeat(3,1fr);gap:12px}
.benefit{height:170px;border:1px solid var(--line);background:#fff;box-shadow:0 2px 4px rgba(0,0,0,.06);text-align:center;padding-top:40px;font-size:13px}
.benefit svg{display:block;margin:0 auto 16px}

/* accreditation */
.badges{top:3350px;left:140px;width:920px;display:flex;justify-content:space-between;align-items:center}
.badge{height:60px;background:#c9d2dc}

/* testimonials / areas */
.testimonials{top:3460px;left:0;width:600px;height:620px;background:var(--navy);color:#fff;padding:50px 60px 0 140px}
.panel-title{font-family:'Oswald','Arial Narrow',sans-serif;text-transform:uppercase;font-size:28px;font-weight:500;color:#fff}
.tabs{position:absolute;right:40px;top:62px;display:flex;gap:6px}
.tabs span{border:1px solid #fff;font-size:9px;padding:3px 10px;text-transform:uppercase}
.tabs span.on{background:#fff;color:var(--navy)}
.quote-mark{font-family:Georgia,serif;font-size:60px;line-height:1;color:#fff;margin:30px 0 -20px -40px}
.testimonials p{font-size:12px;line-height:1.65;margin-bottom:14px}
.testimonials .btn{margin:10px 0 56px}
.testimonials .who{font-size:12px;font-weight:700;text-transform:uppercase}
.dots{position:absolute;left:460px;top:560px;display:flex;gap:8px}
.dots i{width:8px;height:8px;border-radius:50%;background:#56667a}
.dots i.on{background:#fff}
.areas{top:3460px;left:600px;width:600px;height:620px;background:var(--blue);color:#fff;padding:50px 30px 0 30px}
.areas p{font-size:12px;line-height:1.6;margin:16px 0 24px;width:520px}
.cities{display:flex;gap:20px}
.city{width:260px;height:300px;position:relative;background:linear-gradient(180deg,#1c3150 0%,#2f5a8a 45%,#0e1824 100%)}
.city b{position:absolute;left:18px;bottom:14px;font-family:'Oswald','Arial Narrow',sans-serif;font-size:34px;font-weight:500}

/* footer */
.site-footer{top:4080px;left:0;width:1200px;height:340px;background:var(--footer);color:#cfcfcf}
.site-footer .brand{position:absolute;left:140px;top:60px;color:#fff}
.site-footer .brand-square{background:#fff}
.f-col{position:absolute;top:60px;font-size:11px;line-height:1.9}
.f-col h6{font-family:'Oswald','Arial Narrow',sans-serif;font-size:14px;color:#fff;font-weight:500;text-transform:uppercase;margin-bottom:10px}
.f-col li{list-style:none;display:flex;align-items:center;gap:10px}
.dot{width:16px;height:16px;border-radius:50%;background:#555;flex:none}
.copyright{top:4420px;left:0;width:1200px;height:32px;background:#111;color:#999;font-size:10px;text-align:center;line-height:32px}
</style>
</head>
<body>

<header class="site-header abs">
  <div class="brand"><span class="brand-square"></span>Keepsafe Archives</div>
  <a class="btn quote-btn abs">Get a quote now!</a>
  <div class="call abs">
    <span class="call-icon"><svg width="20" height="20" viewBox="0 0 24 24"><path fill="#fff" d="M6.6 10.8a15 15 0 0 0 6.6 6.6l2.2-2.2c.3-.3.7-.4 1-.2 1.1.4 2.3.6 3.6.6.6 0 1 .4 1 1V20c0 .6-.4 1-1 1A17 17 0 0 1 3 4c0-.6.4-1 1-1h3.5c.6 0 1 .4 1 1 0 1.3.2 2.5.6 3.6.1.3 0 .7-.2 1z"/></svg></span>
    <div><small>CALL US</small><strong>1300 555 014</strong></div>
  </div>
  <svg class="cart abs" width="44" height="40" viewBox="0 0 44 40"><path d="M2 4h7l5 22h20l5-15H12" fill="none" stroke="#2d2d2d" stroke-width="3"/><circle cx="16" cy="33" r="3" fill="#2d2d2d"/><circle cx="31" cy="33" r="3" fill="#2d2d2d"/><circle cx="36" cy="8" r="7" fill="#2d2d2d"/><text x="36" y="11" font-size="9" fill="#fff" text-anchor="middle" font-family="Open Sans,sans-serif">0</text></svg>
</header>

<nav class="main-nav abs">
  <a class="active">HOME</a><a>OFFSITE STORAGE</a><a>DOCUMENT SHREDDING</a><a>DIGITISATION</a><a>ARCHIVE SUPPLIES</a><a>CONTACT</a>
</nav>

<section class="hero abs" role="img" aria-label="Man in a shirt reading a document in an archive warehouse with shelving of boxes">
  <h1 class="hero-title head-font abs">Archive Document Storage<br>&amp;Records Management</h1>
  <p class="hero-sub abs" style="top:160px">Professional, secure and reliable. Keepsafe Archives is your total home for all your archiving needs.</p>
  <form class="enquiry abs">
    <h3>Find out how cost effective we are in storing your archive boxes.</h3>
    <div class="field">NAME</div>
    <div class="field">PHONE NUMBER</div>
    <div class="field">EMAIL ADDRESS</div>
    <div class="field select">APPROX. NUMBER OF BOXES</div>
    <span class="send">SEND MESSAGE</span>
  </form>
</section>

<section class="services abs">
  <article class="service s-red"><div class="photo" role="img" aria-label="Warehouse aisle with archive boxes on tall shelves"></div><div class="body"><h4 class="head-font">Offsite Storage</h4><p>Store all your archives in our secure offsite warehouse with fast retrieval.</p></div></article>
  <article class="service s-green"><div class="photo" role="img" aria-label="Pile of shredded paper strips"></div><div class="body"><h4 class="head-font">Document Shredding</h4><p>Lorem ipsum is simply dummy text of the printing and typeset.</p></div></article>
  <article class="service s-orange"><div class="photo" role="img" aria-label="Hands scanning a document on a scanner"></div><div class="body"><h4 class="head-font">Digitisation</h4><p>Lorem ipsum is simply dummy text of the printing and typeset.</p></div></article>
  <article class="service s-blue"><div class="photo" role="img" aria-label="Stacked cardboard archive boxes"></div><div class="body"><h4 class="head-font">Archive Supplies</h4><p>Your one stop shop for all your archiving needs. Shop now.</p></div></article>
</section>

<div class="band abs"></div>
<section class="how abs">
  <h2 class="section-title">How it works</h2>
  <div class="steps">
    <div class="step"><svg width="30" height="30" viewBox="0 0 30 30"><rect x="4" y="10" width="22" height="16" fill="#2f80cf"/><rect x="2" y="5" width="26" height="6" fill="#2469b0"/></svg><div><h5>We deliver boxes and barcodes</h5><p>If you need them, we get you started with all the essentials to prepare your archives.</p></div></div>
    <div class="step"><svg width="30" height="30" viewBox="0 0 30 30"><rect x="6" y="3" width="18" height="24" fill="#2f80cf"/><path d="M10 10h10M10 15h10M10 20h6" stroke="#fff" stroke-width="2"/></svg><div><h5>We pick up your documents</h5><p>When your boxes are ready, let us know and we'll come by and collect your documents.</p></div></div>
    <div class="step"><svg width="30" height="30" viewBox="0 0 30 30"><rect x="3" y="4" width="24" height="6" fill="#2f80cf"/><rect x="3" y="12" width="24" height="6" fill="#2f80cf"/><rect x="3" y="20" width="24" height="6" fill="#2f80cf"/></svg><div><h5>We store your documents</h5><p>Your documents are stored in our secure purpose-built facility in a central location.</p></div></div>
    <div class="step"><svg width="30" height="30" viewBox="0 0 30 30"><rect x="2" y="9" width="17" height="12" fill="#2f80cf"/><path d="M19 12h5l4 5v4h-9z" fill="#2f80cf"/><circle cx="8" cy="23" r="3" fill="#2469b0"/><circle cx="23" cy="23" r="3" fill="#2469b0"/></svg><div><h5>We retrieve &amp; deliver your documents</h5><p>When you need your documents, just call or email us and we'll get them to you!</p></div></div>
    <div class="step" style="border:0"><svg width="30" height="30" viewBox="0 0 30 30"><circle cx="15" cy="15" r="12" fill="#2f80cf"/><path d="M9 15l4 4 8-8" stroke="#fff" stroke-width="3" fill="none"/></svg><div><h5>We can securely destroy</h5><p>We can work with you on determining which documents can be securely destroyed and do this for you.</p></div></div>
  </div>
  <div class="laptop" role="img" aria-label="Laptop with ring binders and a red file standing on the keyboard"></div>
</section>

<section class="team abs" role="img" aria-label="Team of staff in a meeting room by large windows">
  <h2 class="head-font">Our Team</h2>
  <a class="btn">Read more</a>
</section>
<section class="software abs">
  <h2 class="head-font">Indexing Software</h2>
  <p>Say goodbye to the headaches of manually finding your misplaced documents! With our software you can easily locate documents, all of your documents are just a few clicks away.</p>
  <a class="btn">Read more</a>
</section>

<div class="offers-title abs" style="padding-top:40px"><h2 class="section-title center-title">Special Offers</h2></div>
<section class="offers abs">
  <div class="offer o-blue"><h3 class="head-font">Lorem ipsum is simply dummy text of the</h3><a class="btn">Read more</a><div class="offer-badge"><span>GET UPTO</span><b>50%</b><i>OFF</i></div></div>
  <div class="offer o-dark"><h3 class="head-font">Lorem ipsum is simply dummy text of the</h3><a class="btn">Read more</a><div class="offer-badge"><span>GET UPTO</span><b>10%</b><i>OFF</i></div></div>
</section>

<div class="benefits-title abs" style="padding-top:40px"><h2 class="section-title center-title">Benefits</h2></div>
<section class="benefits abs">
  <div class="benefit"><svg width="36" height="36" viewBox="0 0 36 36"><rect x="5" y="7" width="22" height="24" fill="none" stroke="#2f80cf" stroke-width="3"/><path d="M14 22l16-16" stroke="#2f80cf" stroke-width="3"/></svg>No lock-in contracts</div>
  <div class="benefit"><svg width="40" height="36" viewBox="0 0 40 36"><rect x="2" y="10" width="22" height="14" fill="#2f80cf"/><path d="M24 14h7l6 6v4H24z" fill="#2f80cf"/><circle cx="10" cy="27" r="4" fill="#2469b0"/><circle cx="30" cy="27" r="4" fill="#2469b0"/></svg>Speedy Retrievals</div>
  <div class="benefit"><svg width="36" height="36" viewBox="0 0 36 36"><rect x="3" y="9" width="30" height="18" fill="#2f80cf"/><circle cx="18" cy="18" r="5" fill="#fff"/></svg>Money Back<br>Guarantee</div>
  <div class="benefit"><svg width="36" height="36" viewBox="0 0 36 36"><circle cx="18" cy="11" r="7" fill="#2f80cf"/><path d="M5 34c0-9 6-13 13-13s13 4 13 13z" fill="#2f80cf"/></svg>Expert Staff</div>
  <div class="benefit"><svg width="36" height="36" viewBox="0 0 36 36"><circle cx="18" cy="18" r="14" fill="none" stroke="#2f80cf" stroke-width="3"/><path d="M18 9v18M13 13h8a3 3 0 0 1 0 6h-6a3 3 0 0 0 0 6h8" stroke="#2f80cf" stroke-width="2.5" fill="none"/></svg>Competitive<br>Pricing</div>
  <div class="benefit"><svg width="36" height="36" viewBox="0 0 36 36"><circle cx="18" cy="12" r="6" fill="#2f80cf"/><path d="M7 32c0-8 5-11 11-11s11 3 11 11z" fill="#2f80cf"/><path d="M27 6l5 3-5 3" stroke="#2469b0" stroke-width="2" fill="none"/></svg>Simple<br>Online Software</div>
</section>

<section class="badges abs">
  <div class="badge" style="width:150px;border-radius:30px"></div>
  <div class="badge" style="width:110px"></div>
  <div class="badge" style="width:90px;border-radius:50%"></div>
  <div class="badge" style="width:150px;border-radius:30px"></div>
</section>

<section class="testimonials abs">
  <h2 class="panel-title">Testimonials</h2>
  <div class="tabs"><span class="on">Business</span><span>Government</span></div>
  <div class="quote-mark">&ldquo;</div>
  <p>I would like to acknowledge the fantastic job your company has done installing the software and boxes at our school. The efficiency and friendliness of the staff and the minimal disruption to the school during the process was much appreciated.</p>
  <p>Archiving is something that all schools know they have to do but have difficulty finding the time.</p>
  <a class="btn">Read more</a>
  <div class="who">Jane Morrow, Principal</div>
  <div class="dots"><i class="on"></i><i></i><i></i><i></i></div>
</section>
<section class="areas abs">
  <h2 class="panel-title">Areas we service</h2>
  <p>Sed ut perspiciatis unde omnis iste natus error sit voluptatem accusantium doloremque laudantium, totam rem aperiam, eaque ipsa quae ab illo inventore veritatis et quasi architecto beatae vitae dicta sunt explicabo. Nemo enim ipsam voluptatem.</p>
  <div class="cities">
    <div class="city" role="img" aria-label="City skyline at night with river reflections"><b>VIC</b></div>
    <div class="city" role="img" aria-label="Harbour city skyline at dusk"><b>NSW</b></div>
  </div>
</section>

<footer class="site-footer abs">
  <div class="brand"><span class="brand-square"></span>Keepsafe Archives</div>
  <div class="f-col" style="left:480px"><h6>Contact us</h6><ul>
    <li><span class="dot"></span>12 Harbour Lane, Melbourne</li>
    <li><span class="dot"></span>1300 555 014</li>
    <li><span class="dot"></span>(03) 5550 1277</li>
    <li><span class="dot"></span>info@keepsafearchives.example</li></ul></div>
  <div class="f-col" style="left:740px"><h6>Menu</h6><ul>
    <li>HOME</li><li>OFFSITE STORAGE</li><li>DOCUMENT SHREDDING</li><li>DIGITISATION</li><li>ARCHIVE SUPPLIES</li><li>CONTACT US</li></ul></div>
  <div class="f-col" style="left:940px"><h6>Connect with us</h6><ul>
    <li><span class="dot"></span>Social One</li><li><span class="dot"></span>Social Two</li><li><span class="dot"></span>Social Three</li></ul></div>
</footer>
<div class="copyright abs">Copyright &copy; 2016 Keepsafe Archives. All Rights Reserved</div>

</body>
</html>
```